Webpage Design Layout for Thanksgiving/App Charity

Hi,

I am putting together a website called http://kindlyloop.example with the intention of getting app developers to giveaway their usual thanksgiving discount to a charity rather than to the customer.

I am looking for a one page design (not coded) that will have;

1. A header and small description of the idea. For example;

"KindlyLoop - Sharing Makes Ripples"

KindlyLoop is a movement that lets developers and users pass on the usual Thanksgiving discounts to people and communities who need it most. Buy your favourite apps from the links below and 40% of the price goes directly to charity"

2. A small section outlining the charity (not yet selected) with a link to learn more and a 'Play Video' button. I'd like to include a video of the charity.

3. A grid showing the available apps with an 'About' button and 'Buy Now' button

4. a FAQ underneath the apps

5. Some kind of prominent "Money raised" bar that will go near the top of the page

6. A footer section with contact info, mailing list sign up.

7. A countdown timer near the top that will countdown until the charity is over

8. A logo that would represent Apps + Thanksgiving

Obviously since this ties in with thanksgiving and apps I'd like to make it a fun turkey or thanksgiving themed page.

Please use Google Fonts and make sure to have the rights to any images used.

Target Market(s)

I want to appeal to every day phone and computer users. It should be a fun page but that also display credibility and confidence for purchasers/visitors.

Industry/Entity Type

Software

Number of Pages Required

1 page

Requirements
Must have
• Just a fun page that displays credibility and the importance of the idea

```html
<!DOCTYPE html>
<html lang="en">
<head>
<meta charset="utf-8">
<title>KindlyLoop - Sharing Makes Ripples</title>
<link href="https://fonts.googleapis.com/css2?family=Montserrat:wght@300;400;700&family=Open+Sans:wght@400;600;700&display=swap" rel="stylesheet">
<style>
:root{
  --orange:#f4ae4c;
  --white:#ffffff;
  --ink:#333333;
  --muted:#8a8a8a;
  --line:#e4e4e4;
  --faq-bg:#f8f8f8;
  --dark:#282828;
  --darker:#121212;
  --box:#3a3a3a;
}
*{box-sizing:border-box;margin:0;padding:0}
html,body{width:1200px;height:3077px;overflow:hidden}
body{position:relative;font-family:"Open Sans",sans-serif;color:var(--ink);background:var(--white)}
.abs{position:absolute}
.center{left:0;width:1200px;text-align:center}

/* hero */
.hero{top:0;left:0;width:1200px;height:626px;background:radial-gradient(ellipse at 30% 30%,#c8702b 0%,#8a4a1e 35%,#4a2a16 70%,#2b1a10 100%)}
.hero-shade{top:0;left:0;width:1200px;height:626px;background:rgba(0,0,0,.25)}
.logo{left:135px;top:40px;color:var(--white);font-size:17px;font-weight:600}
.nav{top:42px;color:var(--white);font-size:13px;font-weight:700}
.hero-title{top:168px;font-family:"Montserrat",sans-serif;font-weight:700;font-size:34px;color:var(--white)}
.hero-sub{top:220px;font-weight:700;font-size:14px;color:var(--white);letter-spacing:.5px}
.hero-text{top:252px;left:300px;width:600px;text-align:center;font-size:12.5px;line-height:20px;color:var(--white)}
.progress{top:345px;left:355px;width:492px;height:4px;background:rgba(255,255,255,.35)}
.progress-fill{top:345px;left:355px;width:322px;height:4px;background:var(--white)}
.progress-label{top:359px;font-size:9px;font-weight:700;color:#ddd;letter-spacing:1px}
.count-box{top:398px;width:45px;height:43px;border:1px solid rgba(255,255,255,.5);background:rgba(0,0,0,.55);color:var(--orange);font-size:22px;text-align:center;line-height:41px}
.count-sep{top:404px;color:var(--white);font-size:20px}
.count-label{top:446px;width:45px;text-align:center;font-size:9px;color:#ccc;letter-spacing:1px}
.btn-white{top:478px;left:508px;width:159px;height:41px;background:var(--white);color:#222;font-size:12px;font-weight:700;text-align:center;line-height:41px;letter-spacing:.5px}

/* charity */
.charity{top:626px;left:0;width:1200px;height:359px;background:linear-gradient(180deg,#3b3b3b,#2b2b2b 50%,#333)}
.section-title{font-family:"Montserrat",sans-serif;font-weight:400;font-size:28px}
.rule{width:46px;height:3px;left:577px}
.btn{height:39px;font-size:11px;font-weight:700;letter-spacing:1px;text-align:center;line-height:37px}

/* apps */
.card{width:437px;height:221px;background:var(--white);box-shadow:0 1px 8px rgba(0,0,0,.14)}
.card .icon{position:absolute;left:29px;top:40px;width:84px;height:84px;border-radius:10px;background:linear-gradient(135deg,#f08a3c,#c9622a)}
.card h3{position:absolute;left:135px;top:38px;font-family:"Montserrat",sans-serif;font-weight:400;font-size:20px;color:var(--ink)}
.card p{position:absolute;left:135px;top:80px;width:270px;font-size:12.5px;line-height:20px;color:var(--muted)}
.card .links{position:absolute;left:135px;top:162px;font-size:9.5px;font-weight:700;letter-spacing:1px;color:#555}
.card .links .buy{color:var(--orange)}
.card .links .sep{margin:0 18px;color:#bbb;font-weight:400}

/* faq */
.faq{top:1780px;left:0;width:1200px;height:616px;background:var(--faq-bg)}
.faq-item{left:135px;width:454px;height:44px;background:var(--white);border:1px solid var(--line);font-family:"Montserrat",sans-serif;font-size:13.5px;color:var(--ink)}
.faq-item .q{position:absolute;left:20px;top:13px}
.faq-item .sign{position:absolute;right:18px;top:9px;color:var(--orange);font-size:20px;font-weight:300}
.faq-open{height:126px}
.faq-open .bar{position:absolute;left:20px;top:50px;width:414px;height:1px;background:var(--orange)}
.faq-open .a{position:absolute;left:22px;top:64px;width:400px;font-family:"Open Sans",sans-serif;font-size:11.5px;line-height:19px;color:var(--muted)}
.faq-photo{left:683px;top:2016px;width:312px;height:312px;border-radius:50%;background:linear-gradient(180deg,#f2f2f2 0%,#e6e6e6 60%,#dcdcdc 100%)}

/* contact */
.contact{top:2396px;left:0;width:1200px;height:613px;background:var(--dark)}
.field-label{font-size:11.5px;color:#d0d0d0}
.field-line{height:1px;background:#6a6a6a}
.submit{top:2757px;left:533px;width:135px;height:35px;background:var(--orange);color:var(--white);font-size:12px;font-weight:700;letter-spacing:1px;text-align:center;line-height:35px}
.info-box{top:2845px;height:80px;background:var(--box);color:#d8d8d8;font-size:11.5px;line-height:17px}
.info-box svg{position:absolute;top:30px}
.info-box .txt{position:absolute;top:22px}
.footer-links{top:2961px;font-size:10px;color:#c8c8c8;letter-spacing:.5px}
.bottom{top:3009px;left:0;width:1200px;height:68px;background:var(--darker)}
.copy{left:135px;top:3036px;font-size:10px;color:#aaa}
.social{top:3030px;width:28px;height:28px;border:1.5px solid #bbb;border-radius:50%}
</style>
</head>
<body>

<!-- hero -->
<div class="abs hero" role="img" aria-label="Warm autumn table with pumpkins, pine cones and chestnuts on rustic wood"></div>
<div class="abs hero-shade"></div>
<div class="abs logo">Logo</div>
<div class="abs nav" style="left:714px">About</div>
<div class="abs nav" style="left:797px">Charity</div>
<div class="abs nav" style="left:877px">Apps</div>
<div class="abs nav" style="left:950px">FAQs</div>
<div class="abs nav" style="left:1018px">Contact</div>

<h1 class="abs center hero-title">KindlyLoop - Sharing Makes Ripples</h1>
<div class="abs center hero-sub">40% OF ALL PURCHASES GOES TO CHARITY</div>
<p class="abs hero-text">KindlyLoop is a movement that lets developers and users pass on the usual Thanksgiving discounts to people and communities who need it most. Buy your favourite apps from the links below and 40% of the price goes directly to charity.</p>

<div class="abs progress"></div>
<div class="abs progress-fill"></div>
<div class="abs progress-label" style="left:355px">MONEY RAISED</div>
<div class="abs progress-label" style="left:818px">GOAL</div>

<div class="abs count-box" style="left:484px">12</div>
<div class="abs count-sep" style="left:535px">:</div>
<div class="abs count-box" style="left:548px">10</div>
<div class="abs count-sep" style="left:598px">:</div>
<div class="abs count-box" style="left:611px">18</div>
<div class="abs count-sep" style="left:662px">:</div>
<div class="abs count-box" style="left:675px">37</div>
<div class="abs count-label" style="left:484px">DAYS</div>
<div class="abs count-label" style="left:548px">HOUR</div>
<div class="abs count-label" style="left:611px">MIN</div>
<div class="abs count-label" style="left:675px">SEC</div>
<div class="abs btn-white">JOIN US TODAY</div>

<!-- charity -->
<div class="abs charity" role="img" aria-label="Dimmed overhead view of a shared holiday meal table"></div>
<h2 class="abs center section-title" style="top:706px;color:var(--white);font-weight:300">Charity XXXXXXX</h2>
<div class="abs rule" style="top:754px;background:var(--white)"></div>
<p class="abs center" style="top:786px;font-size:12.5px;font-weight:600;color:var(--white)">Charity XXXXX helps children develop the skills they need......</p>
<div class="abs btn" style="top:845px;left:463px;width:126px;background:var(--orange);color:var(--white)">LEARN MORE</div>
<div class="abs btn" style="top:845px;left:603px;width:123px;border:2px solid var(--white);color:var(--white)">PLAY VIDEO</div>

<!-- apps -->
<h2 class="abs center section-title" style="top:1079px;color:var(--ink)">Available Apps</h2>
<div class="abs rule" style="top:1126px;background:#333"></div>

<div class="abs card" style="left:135px;top:1200px">
  <div class="icon" role="img" aria-label="App icon with a festive turkey illustration"></div>
  <h3>Website Builder</h3>
  <p>SiteForge is an easy to use website builder for desktop PCs. The visual website builder is easy to use...</p>
  <div class="links">LEARN MORE<span class="sep">|</span><span class="buy">BUY NOW</span></div>
</div>
<div class="abs card" style="left:628px;top:1200px">
  <div class="icon" style="background:linear-gradient(135deg,#7ec8ef,#c6863f)" role="img" aria-label="App icon with a cartoon turkey illustration"></div>
  <h3>Website Builder</h3>
  <p>SiteForge is an easy to use website builder for desktop PCs. The visual website builder is easy to use...</p>
  <div class="links">LEARN MORE<span class="sep">|</span><span class="buy">BUY NOW</span></div>
</div>
<div class="abs card" style="left:135px;top:1477px">
  <div class="icon" style="background:linear-gradient(135deg,#fbe3b5,#e08a2e)" role="img" aria-label="App icon with a cheerful autumn squirrel illustration"></div>
  <h3>Website Builder</h3>
  <p>SiteForge is an easy to use website builder for desktop PCs. The visual website builder is easy to use...</p>
  <div class="links">LEARN MORE<span class="sep">|</span><span class="buy">BUY NOW</span></div>
</div>
<div class="abs card" style="left:628px;top:1477px">
  <div class="icon" role="img" aria-label="App icon with a festive turkey illustration"></div>
  <h3>Website Builder</h3>
  <p>SiteForge is an easy to use website builder for desktop PCs. The visual website builder is easy to use...</p>
  <div class="links">LEARN MORE<span class="sep">|</span><span class="buy">BUY NOW</span></div>
</div>

<!-- faq -->
<div class="abs faq"></div>
<h2 class="abs center section-title" style="top:1832px;color:var(--ink)">Frequently Asked Questions</h2>
<div class="abs rule" style="top:1880px;background:#333"></div>

<div class="abs faq-item faq-open" style="top:1952px">
  <span class="q">How much money goes charity?</span><span class="sign">&#8212;</span>
  <div class="bar"></div>
  <p class="a">40% off all purchases that go through the Buy Now button for each app goes to charity</p>
</div>
<div class="abs faq-item" style="top:2094px"><span class="q">Question number two here?</span><span class="sign">+</span></div>
<div class="abs faq-item" style="top:2151px"><span class="q">Question number three here?</span><span class="sign">+</span></div>
<div class="abs faq-item" style="top:2211px"><span class="q">Question number four here?</span><span class="sign">+</span></div>
<div class="abs faq-item" style="top:2270px"><span class="q">Question number five here?</span><span class="sign">+</span></div>

<div class="abs faq-photo" role="img" aria-label="Person holding up a sign with a large orange question mark"></div>
<svg class="abs" style="left:615px;top:2170px" width="150" height="90" viewBox="0 0 150 90">
  <path d="M135 8 C120 50 70 75 14 72" fill="none" stroke="#f4ae4c" stroke-width="3"/>
  <path d="M28 58 L12 72 L30 84" fill="none" stroke="#f4ae4c" stroke-width="3" stroke-linecap="round"/>
</svg>

<!-- contact -->
<div class="abs contact"></div>
<h2 class="abs center section-title" style="top:2462px;color:var(--white)">Contact Us</h2>
<div class="abs rule" style="top:2508px;background:var(--white)"></div>

<div class="abs field-label" style="left:303px;top:2574px">First Name</div>
<div class="abs field-line" style="left:303px;top:2598px;width:292px"></div>
<div class="abs field-label" style="left:630px;top:2574px">Last Name</div>
<div class="abs field-line" style="left:630px;top:2598px;width:293px"></div>
<div class="abs field-label" style="left:303px;top:2615px">Email</div>
<div class="abs field-line" style="left:303px;top:2639px;width:292px"></div>
<div class="abs field-label" style="left:630px;top:2615px">Phone</div>
<div class="abs field-line" style="left:630px;top:2639px;width:293px"></div>
<div class="abs field-label" style="left:303px;top:2656px">Message</div>
<div class="abs field-line" style="left:303px;top:2728px;width:620px"></div>
<div class="abs submit">SUBMIT</div>

<div class="abs info-box" style="left:135px;width:296px">
  <svg style="left:38px" width="12" height="16" viewBox="0 0 12 16"><path d="M6 0C2.7 0 0 2.6 0 5.9 0 10 6 16 6 16s6-6 6-10.1C12 2.6 9.3 0 6 0zm0 8.2A2.3 2.3 0 1 1 6 3.6a2.3 2.3 0 0 1 0 4.6z" fill="#f4ae4c"/></svg>
  <div class="txt" style="left:64px">220 Maple Hollow Road, Suite 12<br>Brookfield, TX 70000</div>
</div>
<div class="abs info-box" style="left:455px;width:294px">
  <svg style="left:46px;top:32px" width="14" height="14" viewBox="0 0 14 14"><path d="M3 0l2.5 3.5-1.6 1.6c.8 1.8 2.2 3.2 4 4l1.6-1.6L13 10l-1.6 2.6C6 12.6 1.4 8 1.4 2.6z" fill="#f4ae4c"/></svg>
  <div class="txt" style="left:70px;top:31px">Phone :&nbsp; 555-010-2030</div>
</div>
<div class="abs info-box" style="left:771px;width:295px">
  <svg style="left:44px;top:33px" width="15" height="11" viewBox="0 0 15 11"><rect width="15" height="11" rx="1" fill="#f4ae4c"/><path d="M0 1l7.5 5L15 1" fill="none" stroke="#3a3a3a" stroke-width="1.3"/></svg>
  <div class="txt" style="left:78px;top:31px">Email:&nbsp; info@kindlyloop.example</div>
</div>

<div class="abs center footer-links">HOME &nbsp;|&nbsp; ABOUT US &nbsp;|&nbsp; CHARITY &nbsp;|&nbsp; APPS &nbsp;|&nbsp; FAQS &nbsp;|&nbsp; CONTACT US</div>

<div class="abs bottom"></div>
<div class="abs copy">Copyright © 2017 KindlyLoop. All Rights Reserved.</div>
<div class="abs social" style="left:937px"></div>
<div class="abs social" style="left:971px"></div>
<div class="abs social" style="left:1004px"></div>
<div class="abs social" style="left:1037px"></div>

</body>
</html>
```